2 sided flyer for Insurance Servics

Would like a flyer that talks about who we are, our services, and our process. Attaching relevant information, as well as our Logo and other logos for a few larger insurance carriers that we have access to.

Target Market(s)

Financial Advisors and Insurance Agents

Industry/Entity Type

Finance and Insurance

Colors
0054AA
0677BA
7BADD7
CADEEF
E8F1F8
F0912C
F2A743
F7CA91
FBE8D2
FDF5EE

Requirements
Must have
• Lists, bullet points, pictures, and logos uploaded

```html
<!DOCTYPE html>
<html lang="en">
<head>
<meta charset="UTF-8">
<title>Harborline Risk Partners – Two-Sided Flyer</title>
<link href="https://fonts.googleapis.com/css2?family=Montserrat:wght@500;600;700;800;900&family=Open+Sans:wght@400;600;700&display=swap" rel="stylesheet">
<style>
  :root{
    --navy:#221d45;
    --navy-2:#2e2760;
    --violet:#8677f2;
    --violet-soft:#b9b0fa;
    --lilac:#ece9fe;
    --ink:#2b2b3a;
    --muted:#5d5d70;
    --white:#ffffff;
    --stage:#eeeef3;
  }
  *{box-sizing:border-box;margin:0;padding:0}
  html,body{width:816px;height:1200px;overflow:hidden;background:var(--stage)}
  body{font-family:"Open Sans",Arial,sans-serif;color:var(--ink);position:relative}

  .sheet{position:absolute;top:344px;width:396px;height:512px;overflow:hidden;box-shadow:0 2px 10px rgba(34,29,69,.18)}
  .sheet-front{left:8px}
  .sheet-back{left:412px}
  .page{position:absolute;left:0;top:0;width:816px;height:1056px;background:var(--white);
    transform:scale(.4853);transform-origin:top left;overflow:hidden}

  .display{font-family:"Montserrat",Arial,sans-serif}
  .section-title{font-family:"Montserrat",Arial,sans-serif;font-weight:800;font-size:20px;color:var(--navy);text-transform:uppercase;margin-bottom:12px}
  .hl{color:var(--violet)}
  .body-copy{font-size:12.5px;line-height:1.6;color:var(--muted);margin-bottom:10px}

  /* front */
  .brand{position:absolute;left:40px;top:30px;display:flex;align-items:center;gap:10px}
  .brand-square{width:44px;height:44px;background:var(--navy)}
  .brand-name{font-family:"Montserrat",Arial,sans-serif;font-weight:800;font-size:14px;line-height:1.15;color:var(--navy);letter-spacing:.5px;text-transform:uppercase}
  .hero-photo{position:absolute;left:330px;top:0;width:486px;height:310px;
    background:linear-gradient(135deg,#cfd3e0 0%,#8e8fa6 45%,#3d3a52 100%)}
  .title-panel{position:absolute;left:0;top:104px;width:360px;height:190px;background:var(--navy);padding:26px 30px 0 40px}
  .title-panel h1{font-family:"Montserrat",Arial,sans-serif;font-weight:900;color:var(--white);font-size:38px;line-height:1.04;text-transform:uppercase}
  .title-panel h1 .accent{color:var(--violet-soft)}
  .title-bar{position:absolute;left:40px;bottom:22px;width:70px;height:5px;background:var(--violet)}

  .col-left{position:absolute;left:40px;top:344px;width:280px}
  .col-right{position:absolute;left:360px;top:344px;width:416px}
  .btn{display:inline-block;margin-top:4px;background:var(--violet);color:var(--white);
    font-family:"Montserrat",Arial,sans-serif;font-weight:700;font-size:12px;padding:10px 22px;border-radius:3px}
  .carriers{margin-top:36px}
  .carrier-grid{display:grid;grid-template-columns:repeat(3,1fr);gap:12px;margin-top:4px}
  .carrier-badge{height:40px;background:var(--lilac);border-radius:4px}

  .why-eyebrow{font-family:"Montserrat",Arial,sans-serif;font-weight:800;font-size:20px;color:var(--violet);text-transform:uppercase}
  .why-lead{font-family:"Montserrat",Arial,sans-serif;font-weight:700;font-size:19px;line-height:1.3;color:var(--navy);margin:8px 0 20px}
  .benefit{display:flex;margin-bottom:14px;height:104px}
  .benefit-num{flex:0 0 66px;background:var(--violet);color:var(--white);
    font-family:"Montserrat",Arial,sans-serif;font-weight:900;font-size:36px;display:flex;align-items:center;justify-content:center}
  .benefit-body{flex:1;background:var(--navy);color:var(--white);padding:16px 20px}
  .benefit:nth-child(even) .benefit-body{background:var(--navy-2)}
  .benefit-body h3{font-family:"Montserrat",Arial,sans-serif;font-weight:700;font-size:15px;margin-bottom:6px}
  .benefit-body p{font-size:12.5px;line-height:1.5;color:#d7d3f5}

  .footer{position:absolute;left:0;bottom:0;width:816px;height:76px;background:var(--violet);
    display:flex;align-items:center;justify-content:space-between;padding:0 40px;color:var(--white);
    font-family:"Montserrat",Arial,sans-serif;font-weight:600;font-size:13px}
  .contact{display:flex;align-items:center;gap:8px}
  .contact svg{width:18px;height:18px}
  .web{font-weight:800;font-size:15px}

  /* back */
  .services-band{position:absolute;left:0;top:0;width:816px;height:430px;background:var(--navy);padding:40px 40px 0}
  .services-band .section-title{color:var(--white);font-size:34px;margin-bottom:14px}
  .services-intro{width:380px;font-size:12.5px;line-height:1.6;color:#d7d3f5}
  .quote-card{position:absolute;right:40px;top:36px;width:330px;background:var(--white);border-left:6px solid var(--violet);padding:18px 22px}
  .quote-mark{font-family:"Montserrat",Arial,sans-serif;font-weight:900;font-size:44px;line-height:.8;color:var(--violet)}
  .quote-card p{font-family:"Montserrat",Arial,sans-serif;font-weight:700;font-size:15px;line-height:1.4;color:var(--navy);margin-top:6px}
  .service-row{position:absolute;left:40px;top:218px;width:736px;display:grid;grid-template-columns:repeat(3,1fr);gap:16px}
  .service-card{background:var(--violet);color:var(--white);padding:44px 18px 18px;position:relative;height:176px}
  .service-icon{position:absolute;left:50%;top:-26px;margin-left:-26px;width:52px;height:52px;border-radius:50%;
    background:var(--white);display:flex;align-items:center;justify-content:center}
  .service-icon svg{width:24px;height:24px}
  .service-card h3{font-family:"Montserrat",Arial,sans-serif;font-weight:700;font-size:15px;text-align:center;margin-bottom:8px}
  .service-card p{font-size:12px;line-height:1.5;text-align:center;color:#f1effe}

  .back-left{position:absolute;left:40px;top:462px;width:350px}
  .back-right{position:absolute;left:420px;top:462px;width:356px}
  .pull-quote{border-left:4px solid var(--violet);padding-left:14px;margin-bottom:16px}
  .pull-quote p{font-family:"Montserrat",Arial,sans-serif;font-weight:700;font-size:14px;line-height:1.4;color:var(--navy)}
  .tick-list{list-style:none;margin-top:6px}
  .tick-list li{display:flex;gap:8px;font-size:12.5px;line-height:1.5;color:var(--muted);margin-bottom:6px}
  .tick-list svg{flex:0 0 14px;width:14px;height:14px;margin-top:3px}

  .process-box{background:var(--navy);color:var(--white);padding:22px 22px 14px;margin-top:12px}
  .process-box .section-title{color:var(--white);font-size:20px;margin-bottom:14px}
  .step{display:flex;gap:12px;margin-bottom:12px}
  .step-num{flex:0 0 28px;height:28px;border-radius:50%;background:var(--violet);
    font-family:"Montserrat",Arial,sans-serif;font-weight:800;font-size:13px;display:flex;align-items:center;justify-content:center}
  .step h4{font-family:"Montserrat",Arial,sans-serif;font-weight:700;font-size:13px;margin-bottom:2px}
  .step p{font-size:11.5px;line-height:1.45;color:#d7d3f5}
</style>
</head>
<body>

  <!-- FRONT SIDE -->
  <div class="sheet sheet-front">
    <article class="page page-front">
      <header>
        <div class="brand">
          <span class="brand-square"></span>
          <span class="brand-name">Harborline<br>Risk Partners</span>
        </div>
        <div class="hero-photo" role="img" aria-label="Photo of a team of advisors meeting around a table with a laptop"></div>
        <div class="title-panel">
          <h1>Harborline <span class="accent">Risk</span><br>Partners</h1>
          <span class="title-bar"></span>
        </div>
      </header>

      <section class="col-left">
        <h2 class="section-title">About <span class="hl">Us</span></h2>
        <p class="body-copy">Harborline Risk Partners is an independent brokerage that helps financial advisors and insurance agents place life, disability and long-term care coverage. We pair carrier access with hands-on case design.</p>
        <p class="body-copy">Our team works behind the scenes as an extension of your practice, from first quote to final policy delivery.</p>
        <span class="btn">Learn More About Us</span>
        <div class="carriers">
          <h2 class="section-title">List of <span class="hl">Carriers</span></h2>
          <div class="carrier-grid">
            <span class="carrier-badge"></span><span class="carrier-badge"></span><span class="carrier-badge"></span>
            <span class="carrier-badge"></span><span class="carrier-badge"></span><span class="carrier-badge"></span>
            <span class="carrier-badge"></span><span class="carrier-badge"></span><span class="carrier-badge"></span>
          </div>
        </div>
      </section>

      <section class="col-right">
        <h2 class="why-eyebrow">Why HRP?</h2>
        <p class="why-lead">When you choose to work with us, you add value to your firm, overnight!</p>
        <div class="benefits">
          <div class="benefit"><div class="benefit-num">1</div>
            <div class="benefit-body"><h3>Access to Leading Carriers</h3><p>Quote and place business with a wide panel of highly rated life and annuity carriers.</p></div></div>
          <div class="benefit"><div class="benefit-num">2</div>
            <div class="benefit-body"><h3>Personalized Case Design</h3><p>Our analysts build side-by-side illustrations tailored to each client's goals and budget.</p></div></div>
          <div class="benefit"><div class="benefit-num">3</div>
            <div class="benefit-body"><h3>Streamlined Underwriting</h3><p>We pre-screen cases and manage requirements so approvals move faster.</p></div></div>
          <div class="benefit"><div class="benefit-num">4</div>
            <div class="benefit-body"><h3>Support That Stays</h3><p>From delivery to reviews, we stay on hand to help you serve clients for years.</p></div></div>
        </div>
      </section>

      <footer class="footer">
        <span class="contact">
          <svg viewBox="0 0 24 24" fill="none" stroke="#fff" stroke-width="2" stroke-linecap="round" stroke-linejoin="round"><path d="M22 16.9v3a2 2 0 0 1-2.2 2 19.8 19.8 0 0 1-8.6-3.1 19.5 19.5 0 0 1-6-6A19.8 19.8 0 0 1 2.1 4.2 2 2 0 0 1 4.1 2h3a2 2 0 0 1 2 1.7c.1.9.4 1.8.7 2.7a2 2 0 0 1-.5 2.1L8 9.8a16 16 0 0 0 6 6l1.3-1.3a2 2 0 0 1 2.1-.4c.9.3 1.8.6 2.7.7a2 2 0 0 1 1.7 2z"/></svg>
          (555) 014-2280
        </span>
        <span class="contact">
          <svg viewBox="0 0 24 24" fill="none" stroke="#fff" stroke-width="2" stroke-linejoin="round"><rect x="2" y="4" width="20" height="16" rx="2"/><path d="M22 6l-10 7L2 6"/></svg>
          hello@harborlinerisk.example
        </span>
        <span class="web">www.harborlinerisk.example</span>
      </footer>
    </article>
  </div>

  <!-- BACK SIDE -->
  <div class="sheet sheet-back">
    <article class="page page-back">
      <section class="services-band">
        <h2 class="section-title">Our <span class="hl">Services</span></h2>
        <p class="services-intro">We give advisors and agents a full back office for protection planning: market research, case design, underwriting advocacy and policy service, all under one roof.</p>
        <div class="quote-card">
          <div class="quote-mark">&ldquo;</div>
          <p>Great agents know their numbers. Great partners help them see an opportunity in every case.</p>
        </div>
        <div class="service-row">
          <div class="service-card">
            <span class="service-icon"><svg viewBox="0 0 24 24" fill="none" stroke="#8677f2" stroke-width="2.5" stroke-linecap="round" stroke-linejoin="round"><path d="M4 12l5 5L20 6"/></svg></span>
            <h3>Life Insurance</h3>
            <p>Term, universal and whole life solutions compared across carriers for every client need.</p>
          </div>
          <div class="service-card">
            <span class="service-icon"><svg viewBox="0 0 24 24" fill="none" stroke="#8677f2" stroke-width="2.5" stroke-linecap="round" stroke-linejoin="round"><path d="M4 12h15M13 6l6 6-6 6"/></svg></span>
            <h3>Disability &amp; LTC</h3>
            <p>Income and long-term care protection designed to keep plans on track when life changes.</p>
          </div>
          <div class="service-card">
            <span class="service-icon"><svg viewBox="0 0 24 24" fill="none" stroke="#8677f2" stroke-width="2.5" stroke-linecap="round" stroke-linejoin="round"><path d="M12 21s-7-6.2-7-11a7 7 0 0 1 14 0c0 4.8-7 11-7 11z"/><circle cx="12" cy="10" r="2.5"/></svg></span>
            <h3>Annuities</h3>
            <p>Fixed and indexed options that help clients build and protect reliable retirement income.</p>
          </div>
        </div>
      </section>

      <section class="back-left">
        <div class="pull-quote"><p>Our case designers save you hours on every file so you can focus on clients.</p></div>
        <p class="body-copy">Every case begins with a conversation. We learn about your client, review existing coverage and model options before you ever sit down at the table.</p>
        <ul class="tick-list">
          <li><svg viewBox="0 0 24 24" fill="none" stroke="#8677f2" stroke-width="3" stroke-linecap="round" stroke-linejoin="round"><path d="M4 12l5 5L20 6"/></svg>Side-by-side carrier comparisons</li>
          <li><svg viewBox="0 0 24 24" fill="none" stroke="#8677f2" stroke-width="3" stroke-linecap="round" stroke-linejoin="round"><path d="M4 12l5 5L20 6"/></svg>Informal inquiries and trial applications</li>
          <li><svg viewBox="0 0 24 24" fill="none" stroke="#8677f2" stroke-width="3" stroke-linecap="round" stroke-linejoin="round"><path d="M4 12l5 5L20 6"/></svg>Dedicated case manager on every file</li>
          <li><svg viewBox="0 0 24 24" fill="none" stroke="#8677f2" stroke-width="3" stroke-linecap="round" stroke-linejoin="round"><path d="M4 12l5 5L20 6"/></svg>In-force policy reviews and updates</li>
        </ul>
        <div class="pull-quote" style="margin-top:14px"><p>We grow when you grow, that is the whole model.</p></div>
        <p class="body-copy">There are no fees to join and no production minimums, just tools and people ready to help.</p>
      </section>

      <section class="back-right">
        <p class="body-copy">Whether you place one case a year or one a week, our team adapts to the way you work and the clients you serve.</p>
        <div class="process-box">
          <h2 class="section-title">Our <span class="hl">Process</span></h2>
          <div class="step"><span class="step-num">1</span><div><h4>Discovery Call</h4><p>We review your client's goals, health and budget.</p></div></div>
          <div class="step"><span class="step-num">2</span><div><h4>Case Design</h4><p>Analysts shop the market and prepare clear options.</p></div></div>
          <div class="step"><span class="step-num">3</span><div><h4>Underwriting</h4><p>We order requirements and advocate with carriers.</p></div></div>
          <div class="step"><span class="step-num">4</span><div><h4>Delivery &amp; Service</h4><p>Policies are delivered and reviewed over time.</p></div></div>
        </div>
      </section>

      <footer class="footer">
        <span class="contact">
          <svg viewBox="0 0 24 24" fill="none" stroke="#fff" stroke-width="2" stroke-linecap="round" stroke-linejoin="round"><path d="M22 16.9v3a2 2 0 0 1-2.2 2 19.8 19.8 0 0 1-8.6-3.1 19.5 19.5 0 0 1-6-6A19.8 19.8 0 0 1 2.1 4.2 2 2 0 0 1 4.1 2h3a2 2 0 0 1 2 1.7c.1.9.4 1.8.7 2.7a2 2 0 0 1-.5 2.1L8 9.8a16 16 0 0 0 6 6l1.3-1.3a2 2 0 0 1 2.1-.4c.9.3 1.8.6 2.7.7a2 2 0 0 1 1.7 2z"/></svg>
          (555) 014-2280
        </span>
        <span class="contact">
          <svg viewBox="0 0 24 24" fill="none" stroke="#fff" stroke-width="2" stroke-linejoin="round"><rect x="2" y="4" width="20" height="16" rx="2"/><path d="M22 6l-10 7L2 6"/></svg>
          hello@harborlinerisk.example
        </span>
        <span class="web">www.harborlinerisk.example</span>
      </footer>
    </article>
  </div>

</body>
</html>
```